Re-Brand of TwigLoom along with a new website design

TwigLoom Ltd are a software & database development company using technologies such as PHP, C#, HTML, JQuery, Flex, AS3, MySQL, Oracle, MSSQL. We like to target all types of business from small to large.

We are great at coding but rubbish at design so thats where we need your help!

We want a complete re-brand of TwigLoom including logo, website design, and business cards.

We would like a design that is clean but other than that, please feel free to be creative.

****Logo****
We are looking for a logo that appears professional but with a splash of colour that indicates a creative side. Please see below some logos that we like the look of:

We like this one because it has a nice simple and clear font for the name of the company but also an icon which is colourful and stands out. http://markvault.example/2013/03/brightnook/

We like this one because it is very clean, simple and again very clear. http://markvault.example/2013/03/tallvoices/

http://markvault.example/2013/03/iron-mule/
http://markvault.example/2013/02/brixwell/
http://markvault.example/2013/01/craft-gallery-norland/

As you will see from all of these examples, the font is very clear but there is always a graphic representing the company too. This is what we like.

****Website****
These are some of the examples of websites we like:
https://www.tillquay.example/
https://www.chatterlane.example/home
http://www.gilbertlensworks.example/
http://www.vestano.example/
http://quillmark.example/
https://www.usedealcrate.example/personal-intros
http://www.newtpanel.example/

The current site can be found at twigloom.co.uk

Requirements
Must have
• Website must have the following pages
Home
Services
Projects
About Us
Contact Us

```html
<!DOCTYPE html>
<html lang="en">
<head>
<meta charset="utf-8">
<title>TwigLoom — Home</title>
<link rel="stylesheet" href="https://fonts.googleapis.com/css2?family=Arimo:wght@400;700&family=Noto+Sans:ital,wght@0,400;1,400&display=swap">
<style>
:root{
  --green:#1ee61e;
  --ink:#111111;
  --grey-text:#808080;
  --nav-sub:#b5b5b5;
  --dark-btn:#3c3c3c;
  --rule:#e2e2e2;
  --band:#dadada;
  --footer:#000000;
  --white:#ffffff;
}
*{margin:0;padding:0;box-sizing:border-box}
html,body{width:960px;height:1200px;overflow:hidden;background:var(--white)}
body{position:relative;font-family:"Noto Sans",Verdana,sans-serif;color:var(--ink)}
.abs{position:absolute}

/* header */
.brand{left:102px;top:38px;display:flex;align-items:center;gap:10px}
.brand-dot{width:14px;height:14px;border-radius:50%;background:var(--green)}
.brand-name{font-family:"Arimo",Arial,sans-serif;font-size:32px;font-weight:400;color:#555;letter-spacing:.5px;line-height:36px}
.nav{top:40px;left:0;width:960px}
.nav-item{position:absolute;font-family:"Arimo",Arial,sans-serif}
.nav-item .label{display:block;font-size:12px;color:#222;line-height:16px}
.nav-item .sub{display:block;font-size:11.5px;color:var(--nav-sub);line-height:18px;margin-top:3px}
.nav-item.active .label{color:var(--green)}

/* hero */
.hero-rule{left:0;width:960px;height:3px;background:var(--green)}
.hero{left:0;top:104px;width:960px;height:355px;
  background:radial-gradient(ellipse at 50% 55%,#9aa7b2 0%,#5a6670 35%,#2c343b 70%,#1c2227 100%)}

/* intro columns */
.col{top:512px;width:236px}
.col-head{display:flex;align-items:center;gap:10px;height:24px}
.col-num{width:29px;height:20px;background:linear-gradient(#4a4a4a,#222);color:#fff;border-radius:2px;
  font-family:"Arimo",Arial,sans-serif;font-weight:700;font-size:10px;display:flex;align-items:center;justify-content:center}
.col-title{font-family:"Arimo",Arial,sans-serif;font-size:19px;color:var(--ink)}
.col-rule{position:relative;height:1px;background:var(--green);margin-top:5px}
.col-rule::before{content:"";position:absolute;left:0;top:-1px;width:62px;height:3px;background:var(--green)}
.col-text{margin-top:13px;font-size:10.2px;line-height:14.4px;color:var(--grey-text);text-align:justify}
.btn-more{display:inline-block;margin-top:6px;background:var(--dark-btn);color:#fff;font-size:10px;
  padding:3px 8px;border-radius:2px;letter-spacing:.3px}

/* projects */
.section-title{left:98px;top:716px;font-family:"Arimo",Arial,sans-serif;font-size:19px;font-weight:400;color:var(--ink)}
.pager{top:720px;width:17px;height:16px;border:1px solid #ccc;background:#fff}
.section-rule{left:105px;top:748px;width:751px;height:1px;background:var(--rule)}
.project{top:769px;width:176px}
.project-img{width:176px;height:107px;background:linear-gradient(180deg,#e3dfcf 0%,#c9c7a8 45%,#a6b56e 75%,#8ea54a 100%)}
.project-cap{margin-top:10px;text-align:center;font-size:10.5px;color:var(--ink)}

/* testimonial */
.quote-band{left:0;top:938px;width:960px;height:100px;background:var(--band)}
.quote-mark{left:96px;top:940px;font-family:Georgia,serif;font-size:80px;font-weight:700;color:#fff;line-height:1}
.quote-text{left:141px;top:969px;width:718px;font-style:italic;font-size:10.4px;line-height:14.4px;color:#333}
.quote-author{left:141px;top:1008px;font-size:12px;color:#333}
.quote-author span{font-size:10px;color:#666}
.dots{left:805px;top:953px;display:flex;gap:6px}
.dot{width:8px;height:8px;border-radius:50%;background:#fff}
.dot.on{background:var(--green)}

/* footer */
.footer{left:0;top:1038px;width:960px;height:162px;background:var(--footer);color:#fff}
.socials{position:absolute;left:445px;top:22px;display:flex;gap:17px}
.social{width:10px;height:10px;border-radius:50%;background:#fff}
.f-line{position:absolute;font-size:10.5px;color:#fff;display:flex;align-items:center;gap:6px}
.f-rule{position:absolute;left:341px;top:115px;width:270px;height:1px;background:#fff}
.copy{position:absolute;left:0;width:960px;top:130px;text-align:center;font-size:10px;color:#aaa}
</style>
</head>
<body>

<header>
  <div class="abs brand"><span class="brand-dot"></span><span class="brand-name">TwigLoom</span></div>
  <nav class="abs nav">
    <div class="nav-item active" style="left:430px"><span class="label">Home</span><span class="sub">Source</span></div>
    <div class="nav-item" style="left:516px"><span class="label">About Us</span><span class="sub">Who we are</span></div>
    <div class="nav-item" style="left:614px"><span class="label">Services</span><span class="sub">What we do</span></div>
    <div class="nav-item" style="left:714px"><span class="label">Projects</span><span class="sub">Showcase</span></div>
    <div class="nav-item" style="left:810px"><span class="label">Contact us</span><span class="sub">Just Meet</span></div>
  </nav>
</header>

<div class="abs hero-rule" style="top:100px"></div>
<div class="abs hero" role="img" aria-label="Photo of a person in a dark suit touching a glowing laptop icon surrounded by device icons"></div>
<div class="abs hero-rule" style="top:459px"></div>

<section>
  <article class="abs col" style="left:98px">
    <div class="col-head"><span class="col-num">01</span><span class="col-title">WHO ?</span></div>
    <div class="col-rule"></div>
    <p class="col-text">Lorem ipsum dolor sit amet, consectetur adipiscing elit. Integer ac neque ligula. Pellentesque bibendum, lorem sit amet pretium ultricies, odio purus faucibus eros, a scelerisque orci leo ac libero. Sed fringilla ultricies rutrum. Praesent lacus magna, pharetra eu convallis at, consectetur vitae libero.</p>
    <span class="btn-more">MORE</span>
  </article>
  <article class="abs col" style="left:362px">
    <div class="col-head"><span class="col-num">02</span><span class="col-title">WHAT ?</span></div>
    <div class="col-rule"></div>
    <p class="col-text">Fusce bibendum ante eu urna malesuada eu dapibus magna lobortis. Integer sed nisl at velit vestibulum elementum. Cras et diam turpis. Etiam dictum lobortis felis, eu pulvinar dolor tincidunt a. Proin tincidunt, sem sed dignissim ultricies, tellus dolor scelerisque enim sed ultrices nunc ante vestibulum odio.</p>
    <span class="btn-more">MORE</span>
  </article>
  <article class="abs col" style="left:628px">
    <div class="col-head"><span class="col-num">03</span><span class="col-title">WHY ?</span></div>
    <div class="col-rule"></div>
    <p class="col-text">Curabitur cursus est sit amet dolor pharetra rutrum. Cum sociis natoque penatibus et magnis dis parturient montes, nascetur ridiculus mus. Cras lectus elit, placerat non dapibus et, feugiat sit amet dui. Praesent sollicitudin bibendum erat, vel interdum justo placerat sit amet. Donec facilisis cursus massa nec tincidunt.</p>
    <span class="btn-more">MORE</span>
  </article>
</section>

<section>
  <h2 class="abs section-title">Latest Projects</h2>
  <div class="abs pager" style="left:819px"><svg width="15" height="14"><path d="M9 4 L6 7 L9 10" fill="none" stroke="#aaa" stroke-width="1"/></svg></div>
  <div class="abs pager" style="left:839px"><svg width="15" height="14"><path d="M6 4 L9 7 L6 10" fill="none" stroke="#333" stroke-width="1"/></svg></div>
  <div class="abs section-rule"></div>

  <figure class="abs project" style="left:105px"><div class="project-img" role="img" aria-label="Misty countryside hills with a farmhouse"></div><figcaption class="project-cap">Portfolio Webdesign</figcaption></figure>
  <figure class="abs project" style="left:297px"><div class="project-img" role="img" aria-label="Misty hills with a villa among cypress trees"></div><figcaption class="project-cap">E-commerce Webdesign</figcaption></figure>
  <figure class="abs project" style="left:489px"><div class="project-img" role="img" aria-label="Green rolling fields with a winding track"></div><figcaption class="project-cap">Blogframe theme</figcaption></figure>
  <figure class="abs project" style="left:681px"><div class="project-img" role="img" aria-label="Misty hills with a villa among cypress trees"></div><figcaption class="project-cap">Corporate Webdesign</figcaption></figure>
</section>

<section>
  <div class="abs quote-band"></div>
  <div class="abs quote-mark">&ldquo;</div>
  <div class="abs dots"><span class="dot on"></span><span class="dot"></span><span class="dot"></span><span class="dot"></span></div>
  <p class="abs quote-text">Lorem ipsum dolor sit amet, consectetur adipiscing elit. Integer ac neque ligula. Pellentesque bibendum, lorem sit amet pretium ultricies, odio purus faucibus eros, a scelerisque orci leo ac libero. Sed fringilla ultricies rutrum.</p>
  <p class="abs quote-author">John Doe - <span>Designation</span></p>
</section>

<footer class="abs footer">
  <div class="socials"><span class="social"></span><span class="social"></span><span class="social"></span></div>
  <div class="f-line" style="left:358px;top:54px">
    <svg width="10" height="13" viewBox="0 0 10 13"><path d="M5 0 A5 5 0 0 1 10 5 C10 8 5 13 5 13 C5 13 0 8 0 5 A5 5 0 0 1 5 0Z" fill="#fff"/><circle cx="5" cy="5" r="2" fill="#000"/></svg>
    <span>42 Fernbrook Lane, Ashford, Kent, TN9 4QX</span>
  </div>
  <div class="f-line" style="left:359px;top:88px">
    <svg width="8" height="13" viewBox="0 0 8 13"><rect x="0.5" y="0.5" width="7" height="12" rx="1" fill="none" stroke="#fff"/><rect x="2" y="2" width="4" height="7" fill="#fff"/></svg>
    <span>01632 960 418</span>
  </div>
  <div class="f-line" style="left:468px;top:88px">
    <svg width="13" height="10" viewBox="0 0 13 10"><rect x="0.5" y="0.5" width="12" height="9" fill="none" stroke="#fff"/><path d="M0.5 0.5 L6.5 6 L12.5 0.5" fill="none" stroke="#fff"/></svg>
    <span>contact@twigloom.co.uk</span>
  </div>
  <div class="f-rule"></div>
  <p class="copy">Copyright &copy; 2012 TwigLoom. All rights reserved.</p>
</footer>

</body>
</html>
```